Business card design needed for Renewable utilities company based in New Zealand.

We supply and install solar panels and all components along with it for a fully customisable PV system that helps customer save money on their energy bills right away and also save the planet!

I have attached logo & website design files to give you a better insight.

Business

```html
<!DOCTYPE html>
<html lang="en">
<head>
<meta charset="utf-8">
<title>Brightfield Energy – Business Card</title>
<link href="https://fonts.googleapis.com/css2?family=Open+Sans:wght@400;600&display=swap" rel="stylesheet">
<style>
  :root {
    --page-bg: #e9e7e3;
    --navy-deep: #0c2f5c;
    --navy: #17477f;
    --brand-blue: #1e8fd0;
    --card-white: #f4f4f4;
    --ink: #2a2a2a;
    --on-navy: #e8eef5;
    --link-blue: #3aa3e0;
  }
  * { box-sizing: border-box; margin: 0; padding: 0; }
  html, body { width: 1200px; height: 900px; overflow: hidden; }
  body {
    background: var(--page-bg);
    font-family: "Open Sans", Arial, sans-serif;
    position: relative;
  }
  .card {
    position: absolute;
    left: 320px;
    width: 560px;
    height: 320px;
    border-radius: 4px;
    overflow: hidden;
    box-shadow: 0 8px 22px rgba(0,0,0,.18);
  }
  /* Front */
  .card-front {
    top: 75px;
    background: radial-gradient(ellipse at 35% 35%, var(--navy) 0%, var(--navy-deep) 75%);
    color: var(--on-navy);
  }
  .front-texture {
    position: absolute;
    right: 40px; top: 50px;
    width: 300px; height: 170px;
    background: radial-gradient(ellipse at center, rgba(120,170,220,.22), rgba(120,170,220,0) 70%);
  }
  .front-brand {
    position: absolute;
    left: 48px; top: 46px;
    display: flex; align-items: center; gap: 14px;
  }
  .brand-dot {
    width: 44px; height: 44px; border-radius: 50%;
    background: var(--on-navy);
  }
  .front-brand .brand-name {
    font-size: 26px; font-weight: 400; color: var(--on-navy); letter-spacing: .3px;
  }
  .front-rule {
    position: absolute; right: 48px; bottom: 82px;
    width: 200px; border-top: 2px dotted var(--link-blue);
  }
  .front-web {
    position: absolute; right: 48px; bottom: 50px;
    font-size: 14px; color: var(--link-blue);
  }
  /* Back */
  .card-back {
    top: 475px;
    background: var(--card-white);
    color: var(--ink);
  }
  .back-brand {
    position: absolute; left: 40px; top: 34px;
    display: flex; align-items: center; gap: 10px;
  }
  .back-brand .brand-dot { width: 38px; height: 38px; background: var(--brand-blue); }
  .back-brand .brand-name { font-size: 21px; color: var(--brand-blue); }
  .person { position: absolute; left: 150px; top: 100px; width: 300px; }
  .person-name { font-size: 22px; letter-spacing: .5px; }
  .person-role {
    text-align: right; font-size: 13px; color: var(--brand-blue);
    padding-bottom: 8px; border-bottom: 2px dotted var(--brand-blue); margin-top: 2px;
  }
  .details {
    position: absolute; left: 150px; top: 178px; right: 36px;
    display: flex; justify-content: space-between;
    font-size: 13px; line-height: 1.35;
  }
  .label { color: var(--brand-blue); display: block; }
  .contact-item { margin-bottom: 4px; }
  .address { text-align: right; align-self: flex-end; padding-bottom: 6px; }
</style>
</head>
<body>
  <section class="card card-front">
    <div class="front-texture" role="img" aria-label="Faint dotted world map pattern"></div>
    <div class="front-brand">
      <span class="brand-dot"></span>
      <span class="brand-name">Brightfield Energy</span>
    </div>
    <div class="front-rule"></div>
    <div class="front-web">www.brightfieldenergy.co</div>
  </section>

  <section class="card card-back">
    <div class="back-brand">
      <span class="brand-dot"></span>
      <span class="brand-name">Brightfield Energy</span>
    </div>
    <div class="person">
      <div class="person-name">MARA ELLISON</div>
      <div class="person-role">Manager</div>
    </div>
    <div class="details">
      <div class="contacts">
        <div class="contact-item"><span class="label">Mobile</span>021 555 0142</div>
        <div class="contact-item"><span class="label">Phone</span>09 555 0187</div>
        <div class="contact-item"><span class="label">Email</span>ellison@brightfieldenergy.co</div>
      </div>
      <div class="address">120 Harbour Road<br>Level 4<br>Auckland 1010</div>
    </div>
  </section>
</body>
</html>
```